Office Technology Business Card Design for B2B sales people

I am looking to get a complete redesign of our company business card. It may just be my card that gets updated but I am looking for ideas that will ultimately make me/us proud to leave our business card with prospective and current clients.

The sky is the limit in terms of design. We have two logos to choose from and we must have Quilvor logo on the card somewhere.

I have uploaded a sample of our current card (which I do not like so it is for reference only)

I have also uploaded two logos to play around with.

On the logo that says Performing Daily under the TOE we are going to be removing that phrase and simply putting Tarnwell Office Equipment.

I am looking for both back and Front. Feel free to check out our website and look for content for the back. I am not sure if I want to highlight a few of the more popular solutions that we sell or just leave it with design and no content.

Once again looking for a complete redesign that is Modern, Simple, has a quick "Wow thats impressive" factor when leaving it behind.

www.toenet-example.com

Industry/Entity Type

Business

Contact Information for Business Card

Must Contain Name, Title, Email, Office Phone, Cell Phone, Address, logo, and quilvor log followed by A quilvor Company. This can be anywhere on the card and does not have to in conjunction with company logo.

Requirements
Must have
• Modern Look and communicates information cleary but pops out as impressive card.
Should not have
• very generic template

```html
<!DOCTYPE html>
<html lang="en">
<head>
<meta charset="utf-8">
<title>TOE Business Card – Front and Back</title>
<link rel="stylesheet" href="https://fonts.googleapis.com/css2?family=Bebas+Neue&family=Lato:wght@400;700&display=swap">
<style>
  :root {
    --backdrop: #b9cbd3;
    --blue-deep: #0a4aa6;
    --blue-mid: #0a86c6;
    --blue-light: #4cc6df;
    --navy: #2a5597;
    --title-blue: #1c5bb0;
    --mission-cyan: #1aa7d2;
    --icon-navy: #1c4f8c;
    --white: #ffffff;
    --pattern-tint: #c9cfe8;
  }
  * { box-sizing: border-box; margin: 0; padding: 0; }
  html, body { width: 1200px; height: 1200px; overflow: hidden; }
  body { background: var(--backdrop); position: relative; font-family: "Lato", sans-serif; }

  .card { position: absolute; left: 183px; width: 836px; background: var(--white); overflow: hidden;
          box-shadow: 0 14px 18px -10px rgba(40,60,80,.35); }
  .card--front { top: 73px; height: 477px; }
  .card--back { top: 647px; height: 476px; }

  /* front */
  .front-panel { position: absolute; inset: 0 0 83px 0;
    background: linear-gradient(125deg, var(--blue-deep) 0%, var(--blue-mid) 55%, var(--blue-light) 100%); }
  .front-panel::after { content: ""; position: absolute; left: 0; right: 0; bottom: 0; height: 22px;
    background: linear-gradient(to bottom, transparent, rgba(0,40,90,.35)); }
  .company { position: absolute; left: 70px; top: 130px; width: 270px; text-align: center; }
  .company-name { font-family: "Lato", sans-serif; font-weight: 700; font-size: 34px; line-height: 42px; color: var(--white); }
  .partner { position: absolute; left: 88px; top: 312px; display: flex; align-items: center; gap: 16px; }
  .partner-name { font-family: "Lato", sans-serif; font-weight: 700; font-size: 19px; color: var(--white); }
  .partner-tag { font-family: "Bebas Neue", sans-serif; font-size: 17px; color: var(--white); letter-spacing: .3px; }
  .divider { position: absolute; left: 409px; top: 55px; width: 3px; height: 305px;
    background: linear-gradient(to bottom, transparent, rgba(10,40,90,.75) 30%, rgba(10,40,90,.75) 70%, transparent); }
  .service-icon { position: absolute; width: 88px; height: 88px; border-radius: 50%; background: var(--white);
    display: flex; align-items: center; justify-content: center; }
  .service-icon svg { width: 48px; height: 48px; fill: var(--icon-navy); }

  .mission { position: absolute; left: 0; right: 0; bottom: 0; height: 83px; }
  .pattern { position: absolute; opacity: .7; }
  .mission .pattern { right: 0; top: 0; width: 320px; height: 83px;
    background: linear-gradient(135deg, rgba(255,255,255,0) 0%, var(--pattern-tint) 55%, rgba(255,255,255,0.2) 100%); }
  .mission-text { position: relative; text-align: center; color: var(--mission-cyan); font-size: 18px; line-height: 22px; padding-top: 15px; }

  /* back */
  .card--back .pattern { left: 0; top: 0; width: 836px; height: 250px;
    background: linear-gradient(120deg, rgba(255,255,255,0) 10%, var(--pattern-tint) 60%, rgba(255,255,255,.3) 100%); opacity: .55; }
  .person { position: absolute; left: 0; right: 0; top: 74px; text-align: center; }
  .person-name { font-family: "Bebas Neue", sans-serif; font-weight: 400; font-size: 92px; line-height: 84px; color: var(--navy); letter-spacing: 1px; }
  .person-title { font-family: "Bebas Neue", sans-serif; font-size: 36px; line-height: 36px; color: var(--title-blue); margin-top: 0; }
  .contact-band { position: absolute; left: 0; right: 0; top: 251px; height: 152px;
    background: linear-gradient(90deg, var(--blue-deep) 0%, var(--blue-mid) 60%, var(--blue-light) 100%);
    color: var(--white); font-size: 22px; box-shadow: 0 -6px 10px -6px rgba(0,0,0,.25), 0 8px 12px -6px rgba(0,0,0,.25); }
  .address { position: absolute; left: 65px; top: 24px; line-height: 29px; }
  .contact-list { position: absolute; left: 436px; top: 18px; list-style: none; }
  .contact-list li { display: flex; align-items: center; height: 41px; }
  .contact-list svg { width: 28px; height: 34px; margin-right: 22px; fill: none; stroke: var(--white); stroke-width: 1.6; }
</style>
</head>
<body>

<section class="card card--front">
  <div class="front-panel">
    <div class="company"><p class="company-name">Tarnwell<br>Office Equipment</p></div>
    <div class="partner">
      <span class="partner-name">quilvor</span>
      <span class="partner-tag">A QUILVOR COMPANY</span>
    </div>
    <div class="divider"></div>

    <div class="service-icon" style="left:520px;top:91px">
      <svg viewBox="0 0 48 48"><path d="M17 10h14a3 3 0 0 1 3 3v3h8a3 3 0 0 1 3 3v7H3v-7a3 3 0 0 1 3-3h8v-3a3 3 0 0 1 3-3zm1 6h12v-2H18zM3 29h18v3h6v-3h18v9a3 3 0 0 1-3 3H6a3 3 0 0 1-3-3z"/></svg>
    </div>
    <div class="service-icon" style="left:651px;top:91px">
      <svg viewBox="0 0 48 48"><path d="M13 5h18l5 5v9H13zM6 21h36a3 3 0 0 1 3 3v12h-7v-6H10v6H3V24a3 3 0 0 1 3-3zm7 12h22v10H13z"/></svg>
    </div>
    <div class="service-icon" style="left:523px;top:206px">
      <svg viewBox="0 0 48 48"><path d="M19 7c9 0 16 5 16 12s-7 12-16 12c-2 0-3 0-5-1l-8 4 3-7c-4-2-6-5-6-8C3 12 10 7 19 7zm19 10c5 2 8 6 8 10 0 3-2 6-5 8l2 6-7-4c-2 1-3 1-5 1-5 0-9-2-12-5 9-1 17-7 19-16z"/></svg>
    </div>
    <div class="service-icon" style="left:653px;top:206px">
      <svg viewBox="0 0 48 48"><path d="M42 12l-7 7-6-1-1-6 7-7c-6-2-13 2-13 9 0 1 0 3 1 4L5 36a4 4 0 0 0 6 6l18-18c8 3 15-4 13-12z"/></svg>
    </div>
  </div>
  <div class="mission">
    <div class="pattern" role="img" aria-label="Soft pattern of overlapping translucent squares"></div>
    <p class="mission-text">At TOE, it’s our mission to provide &nbsp;an un-paralleled customer experience<br>through the power of people, technology and innovation.</p>
  </div>
</section>

<section class="card card--back">
  <div class="pattern" role="img" aria-label="Soft pattern of overlapping translucent squares"></div>
  <div class="person">
    <h1 class="person-name">DORIAN HALE</h1>
    <p class="person-title">SOLUTIONS SPECIALIST</p>
  </div>
  <div class="contact-band">
    <p class="address">418 W. Larkfield Court<br>Marrow Falls, ID 83999</p>
    <ul class="contact-list">
      <li><svg viewBox="0 0 28 34"><rect x="4" y="1" width="20" height="32" rx="3"/><line x1="4" y1="6" x2="24" y2="6"/><line x1="4" y1="27" x2="24" y2="27"/></svg>cell phone</li>
      <li><svg viewBox="0 0 28 34"><circle cx="14" cy="17" r="5"/><path d="M19 13v6a3 3 0 0 0 6 0v-2a11 11 0 1 0-5 9"/></svg>dhale@toenet-example.com</li>
      <li><svg viewBox="0 0 28 34"><path d="M3 2l20 15-9 1 5 11-4 2-5-11-7 6z"/></svg>www.toenet-example.com</li>
    </ul>
  </div>
</section>

</body>
</html>
```